Mobile App UI for Telecommunications/Hosting Company

We are about to convert our existing self-service Customer Portal into a mobile phone application and need an elegant and professional UI/UX design. Our company provides telecommunication (voice/mobile/data) and hosting services to medium-sized business. The primary purpose of the application is to view trouble tickets, alerts, orders, and performance charts. This application is available to customers only - not the general public.

Please provide a UI design suitable for display on iPhone/Android devices. The attached document includes a proposed screen flow. You are free to design your own screens to display the same information elegantly.
Updates

Please note that the design should be based on the wireframes in the Word document, not the screenshots.  The screenshots are just to show our existing web portal look & feel.

Also, just a few screens are required for initial submission (3 would be great).

Thanks,
Dermot.

Target Market(s)

IT Managers away from their desk and using a mobile phone application.
Adult males from technical background aged 30-50.
Customers of Brindlewood Networks have access to this application (not the general public). This is a self-service portal for customers only.

Industry/Entity Type

Business

Colors
0592cd
33a6d7
85cae6
cadf82
fde08a

Requirements
Must have
• Please look at the screenshots from our current Customer Portal site (part of the project brief). The mobile app does not have to look the same, but should follow a similar style.

Please check out our company web site at www.brindlewoodnetworks.example (this site is not the customer portal and has a different look at feel) to understand what Brindlewood Networks does.
Nice to have
• Sharing capabilities via email/SMS.
A nice background image to make it stand out
The colours selected below are a guide only as they are similar to the corporate colours
- The priority is something that works on a phone - a design extendable to tablets is a nice to have as our existing web site looks OK on a tablet..

```html
<!DOCTYPE html>
<html lang="en">
<head>
<meta charset="utf-8">
<title>Brindlewood Networks – Menu</title>
<link rel="stylesheet" href="https://fonts.googleapis.com/css2?family=Open+Sans:wght@400;600&display=swap">
<style>
  :root{
    --drawer-yellow:#f1e18e;
    --divider:#e2d07c;
    --icon-cream:#fbf3cf;
    --label-grey:#5f5b52;
    --badge-dark:#5d5a55;
    --white:#ffffff;
    --sky-light:#86c8df;
    --sky-deep:#3aa3c8;
    --list-bg:#eeeeea;
    --list-row-alt:#dcdcd7;
    --list-text:#b9b9b4;
    --alert-pink:#e0557a;
  }
  *{box-sizing:border-box;margin:0;padding:0}
  html,body{width:676px;height:1200px;overflow:hidden;background:#fff}
  body{font-family:"Open Sans",Arial,sans-serif;position:relative}

  /* Underlying dashboard screen */
  .dashboard{position:absolute;inset:0;background:var(--list-bg)}
  .dashboard-top{position:absolute;left:0;top:0;width:676px;height:127px;background:linear-gradient(90deg,#9fd3e3,var(--sky-light))}
  .profile-icon{position:absolute;left:587px;top:24px;width:52px;height:54px}
  .dashboard-hero{position:absolute;left:0;top:127px;width:676px;height:232px;background:linear-gradient(180deg,#4fb0d2,var(--sky-deep) 60%,#7ec3da)}
  .hero-count{position:absolute;left:410px;top:20px;font-size:150px;line-height:1;color:var(--white);font-weight:400}
  .alert-list{position:absolute;left:0;top:359px;width:676px;list-style:none}
  .alert-row{height:127px;border-bottom:2px solid #e3e3de;background:linear-gradient(90deg,#f6f5f1,#ecebe6);display:flex;align-items:center;padding-left:510px;font-size:36px;color:var(--list-text)}
  .alert-row.is-critical{background:var(--list-row-alt);color:var(--alert-pink)}

  /* Navigation drawer */
  .drawer{position:absolute;left:0;top:0;width:532px;height:1200px;background:var(--drawer-yellow);box-shadow:4px 0 10px rgba(0,0,0,.08)}
  .drawer-header{position:relative;height:300px;background:linear-gradient(180deg,#8fc6c9 0%,#c7d3b4 45%,#d3c59c 75%,#c8b48c 100%)}
  .avatar{position:absolute;left:173px;top:30px;width:194px;height:194px;border-radius:50%;border:6px solid var(--white);background:radial-gradient(circle at 50% 40%,#b79a86,#6f6a64 70%,#4e5054)}
  .user-name{position:absolute;left:0;right:0;top:238px;text-align:center;color:var(--white);font-size:30px;font-weight:600}
  .close-btn{position:absolute;left:466px;top:30px;width:34px;height:34px}

  .menu{list-style:none}
  .menu-item{position:relative;height:126px;border-bottom:2px solid var(--divider);display:flex;align-items:center}
  .menu-icon{position:absolute;left:22px;width:50px;height:50px}
  .menu-label{position:absolute;left:108px;font-size:36px;color:var(--label-grey);letter-spacing:.5px}
  .badge{position:absolute;left:427px;width:78px;height:48px;border-radius:24px;background:var(--badge-dark);color:var(--white);font-size:30px;display:flex;align-items:center;justify-content:center}
  .badge.is-light{background:var(--white);color:var(--label-grey)}
  .support-line{position:absolute;left:20px;top:1106px;font-size:27px;color:var(--label-grey)}
</style>
</head>
<body>

<main class="dashboard">
  <div class="dashboard-top">
    <svg class="profile-icon" viewBox="0 0 52 54" fill="none" stroke="#fff" stroke-width="3.5">
      <circle cx="26" cy="17" r="13"/>
      <path d="M3 52c0-13 10-21 23-21s23 8 23 21z"/>
    </svg>
  </div>
  <div class="dashboard-hero"><span class="hero-count">24</span></div>
  <ul class="alert-list">
    <li class="alert-row">warning</li>
    <li class="alert-row is-critical">warning</li>
    <li class="alert-row">warning</li>
    <li class="alert-row">warning</li>
    <li class="alert-row">warning</li>
    <li class="alert-row">warning</li>
  </ul>
</main>

<nav class="drawer">
  <header class="drawer-header">
    <div class="avatar" role="img" aria-label="Profile photo of the signed-in user"></div>
    <p class="user-name">User Rowan</p>
    <svg class="close-btn" viewBox="0 0 34 34" stroke="#fff" stroke-width="6" stroke-linecap="round">
      <path d="M4 4L30 30M30 4L4 30"/>
    </svg>
  </header>

  <ul class="menu">
    <li class="menu-item">
      <svg class="menu-icon" viewBox="0 0 50 50" fill="none" stroke="var(--icon-cream)" stroke-width="3" stroke-linejoin="round">
        <rect x="4" y="11" width="42" height="29" rx="4"/><path d="M5 13l20 15 20-15"/>
      </svg>
      <span class="menu-label">ALERTS</span><span class="badge">24</span>
    </li>
    <li class="menu-item">
      <svg class="menu-icon" viewBox="0 0 50 50" fill="none" stroke="var(--icon-cream)" stroke-width="3" stroke-linejoin="round">
        <path d="M4 24L46 6 38 44 24 32 4 24z"/><path d="M24 32l22-26M24 32v12l6-7"/>
      </svg>
      <span class="menu-label">ORDERS</span><span class="badge is-light">3</span>
    </li>
    <li class="menu-item">
      <svg class="menu-icon" viewBox="0 0 50 50" fill="none" stroke="var(--icon-cream)" stroke-width="3" stroke-linejoin="round">
        <rect x="5" y="9" width="40" height="36" rx="3"/><path d="M14 4v10M36 4v10M5 19h40"/>
        <path d="M13 27h4M23 27h4M33 27h4M13 36h4M23 36h4M33 36h4"/>
      </svg>
      <span class="menu-label">TICKETS</span><span class="badge">5</span>
    </li>
    <li class="menu-item">
      <svg class="menu-icon" viewBox="0 0 50 50" fill="none" stroke="var(--icon-cream)" stroke-width="3" stroke-linejoin="round" stroke-linecap="round">
        <path d="M3 34l12-11 9 7 12-12 11 9"/>
      </svg>
      <span class="menu-label">CHARTS</span>
    </li>
    <li class="menu-item">
      <svg class="menu-icon" viewBox="0 0 50 50" fill="none" stroke="var(--icon-cream)" stroke-width="3" stroke-linecap="round">
        <circle cx="25" cy="25" r="20"/><path d="M25 15v20M15 25h20"/>
      </svg>
      <span class="menu-label">ADDRESS</span>
    </li>
    <li class="menu-item">
      <svg class="menu-icon" viewBox="0 0 50 50" fill="none" stroke="var(--icon-cream)" stroke-width="3" stroke-linejoin="round">
        <path d="M21 4h8l1 6 5 2 5-4 6 6-4 5 2 5 6 1v8l-6 1-2 5 4 5-6 6-5-4-5 2-1 6h-8l-1-6-5-2-5 4-6-6 4-5-2-5-6-1v-8l6-1 2-5-4-5 6-6 5 4 5-2z"/>
        <circle cx="25" cy="25" r="8"/>
      </svg>
      <span class="menu-label">SETTINGS</span>
    </li>
  </ul>

  <p class="support-line">Support line:&nbsp; 481 - 2976 -3184</p>
</nav>

</body>
</html>
```